Business Cards for IT Consulting Company (Managed Service Provider)

I am looking to have some business cards printed and would like some designs. We are an IT Consulting company based in Vancouver BC. I would like a nice clean and modern look to the cards. I have uploaded all the versions of my logo so parts can be used as needed. Here is a snippit from our website homepage:

Kelbrook Systems Ltd. is an IT Solutions Partner located in Vancouver BC, Canada. We offer IT solutions and support to customers in the greater Vancouver Area. With expertise in Microsoft platforms, as well as Linux and Mac OSX and over 12 years experience in the IT industry, Kelbrook Systems is dedicated to offering our clients top quality service and products. We take pride in the solutions we offer our customers. The greatest compliment a client can give us is to recommend our services.

Kelbrook Systems Ltd. offers a wide range of IT services from onsite service to remote support and managed service solutions. This allows clients to choose the support path that best suits their company’s needs. Supporting many different sized companies from small to enterprise level over the past 12 years Kelbrook Systems has the experience and expertise needed to ensure things run smoothly. Allowing our clients to focus on doing business.

Revolutionizing the way IT services are delivered.

Kelbrook Systems is dedicated to providing our clients with IT solutions that work and grow with them for years to come. This philosophy helps save money in the long run instead of replacing equipment constantly. Far too often IT solutions are not well thought out and while possibly solving the problem at hand, require replacement due to growth or quality within a very short time frame. Kelbrook Systems takes pride in providing solutions that will last and be able to accommodate growth without the need for replacement.

Industry/Entity Type

Information Technology

Contact Information for Business Card

Kelbrook Systems Ltd.
(Employee Name)
Eml: (Employees Email Address)
Web: kelbrook.me
Ph: 604-555-0142

Font styles to use
Serif
Sans Serif

Requirements
Must have
• The Company logo and company colors.
Nice to have
• - Our tag line: "Revolutionizing IT Services" or "Revolutionizing the way IT services are delivered."
• - Also I really like the idea of nature and technology together blending which is sort of where my logo came from so integrating that somehow onto the business cards would be great.

```html
<!DOCTYPE html>
<html lang="en">
<head>
<meta charset="utf-8">
<title>Kelbrook Systems Ltd. — Business Cards</title>
<link rel="stylesheet" href="https://fonts.googleapis.com/css2?family=Montserrat:wght@500;700&family=Tinos:ital,wght@0,400;1,700&display=swap">
<style>
  :root {
    --canvas: #ececec;
    --card: #f7f7f7;
    --brand-blue: #2aa6e0;
    --brand-grey: #6b6e72;
    --white: #ffffff;
  }
  * { box-sizing: border-box; margin: 0; padding: 0; }
  html, body { width: 1200px; height: 800px; overflow: hidden; }
  body {
    background: var(--canvas);
    position: relative;
    font-family: "Montserrat", Arial, sans-serif;
  }
  .card {
    position: absolute;
    width: 480px;
    height: 274px;
    background: var(--card);
    box-shadow: 0 10px 30px rgba(0,0,0,0.12), 0 2px 4px rgba(0,0,0,0.08);
    overflow: hidden;
  }
  .card--front { left: 90px; top: 300px; }
  .card--back  { left: 630px; top: 230px; }

  .wordmark {
    display: flex;
    align-items: center;
    gap: 10px;
    color: var(--brand-grey);
    font-weight: 700;
    letter-spacing: 0.5px;
  }
  .wordmark__mark {
    width: 22px;
    height: 22px;
    border: 3px solid var(--brand-blue);
    flex: none;
  }

  .card--front .wordmark {
    position: absolute;
    left: 0; right: 0; top: 92px;
    justify-content: center;
    font-size: 28px;
  }
  .tagline {
    position: absolute;
    left: 0; right: 0; top: 160px;
    text-align: center;
    font-family: "Tinos", "Times New Roman", serif;
    font-style: italic;
    font-weight: 700;
    font-size: 15px;
    color: var(--brand-blue);
    letter-spacing: 0.3px;
  }

  .card--back .wordmark {
    position: absolute;
    left: 32px; top: 40px;
    font-size: 22px;
  }
  .contact-panel {
    position: absolute;
    left: 150px; right: 0;
    top: 120px; bottom: 22px;
    background: var(--brand-blue);
    color: var(--white);
  }
  .contact-panel__stripes {
    position: absolute;
    left: 0; top: 62px;
    width: 110px; height: 70px;
  }
  .employee-name {
    position: absolute;
    left: 118px; top: 14px;
    font-size: 19px;
    font-weight: 700;
    letter-spacing: 0.5px;
  }
  .contact-list {
    position: absolute;
    left: 118px; top: 52px;
    list-style: none;
    font-family: "Tinos", "Times New Roman", serif;
    font-size: 14px;
    line-height: 22px;
  }
  .contact-list li { display: flex; align-items: center; gap: 8px; }
  .contact-list svg { width: 12px; height: 12px; flex: none; }
</style>
</head>
<body>

  <section class="card card--front" aria-label="Card front">
    <div class="wordmark"><span class="wordmark__mark"></span>Kelbrook Systems Ltd.</div>
    <p class="tagline">Revolutionizing the way IT services are delivered</p>
  </section>

  <section class="card card--back" aria-label="Card back">
    <div class="wordmark"><span class="wordmark__mark"></span>Kelbrook Systems Ltd.</div>
    <div class="contact-panel">
      <svg class="contact-panel__stripes" viewBox="0 0 110 70" aria-hidden="true">
        <g fill="#ffffff">
          <rect x="0" y="0"  width="110" height="5"/>
          <rect x="0" y="14" width="110" height="5"/>
          <rect x="0" y="28" width="110" height="5"/>
          <rect x="0" y="42" width="110" height="5"/>
          <rect x="0" y="56" width="110" height="5"/>
        </g>
      </svg>
      <p class="employee-name">Employee Name</p>
      <ul class="contact-list">
        <li>
          <svg viewBox="0 0 12 12" aria-hidden="true"><path d="M3 1 L5 3.5 L4 5 Q5 7 7 8 L8.5 7 L11 9 L9.5 11 Q4 10.5 1 3 Z" fill="#fff"/></svg>
          604-555-0142
        </li>
        <li>
          <svg viewBox="0 0 12 12" aria-hidden="true"><rect x="0.75" y="2" width="10.5" height="8" fill="none" stroke="#fff" stroke-width="1.2"/><path d="M1 2.5 L6 6.5 L11 2.5" fill="none" stroke="#fff" stroke-width="1.2"/></svg>
          Employee Email Address
        </li>
        <li>
          <svg viewBox="0 0 12 12" aria-hidden="true"><circle cx="6" cy="6" r="5" fill="none" stroke="#fff" stroke-width="1.2"/><ellipse cx="6" cy="6" rx="2.2" ry="5" fill="none" stroke="#fff" stroke-width="1"/><path d="M1 6 H11" stroke="#fff" stroke-width="1"/></svg>
          www.kelbrook.me
        </li>
      </ul>
    </div>
  </section>

</body>
</html>
```